7TallHarbor.com - website redesign

We need to redesign 7TallHarbor.com.
Here are design specs: https://files.quillmarsh.net/deck/8hRkw2LpZn4QvTs0YbXe6MuAcJd9FgNo3WiKl/view?mode=shared

Here is a video going over the design specs:
https://media.quillmarsh.net/clip/d/9x47ruQmTb3HnKcWvZ8oEsYa2LfJ-/play?mode=shared
Updates

I am moving houses on June 10th. Movers are already scheduled.

Target Market(s)

Seattle, WA

Number of Pages Required

2 page

Font styles to use
Serif

Colors

Designer to choose colors to be used in the design.

Requirements
Must have
• Desktop and Mobile Designs
Use colors from their logo....as provided in the design specs document.

Should not have
• Please follow design specs as provided in Seekly Slides. Must watch the video to understand what's needed.

```html
<!DOCTYPE html>
<html lang="en">
<head>
<meta charset="utf-8">
<title>7 Tall Harbor – Certified E-Recycling</title>
<link href="https://fonts.googleapis.com/css2?family=Noto+Serif:wght@400;700&display=swap" rel="stylesheet">
<style>
:root{
  --green:#179a47;
  --lime:#85c227;
  --ink:#1b1b1b;
  --muted:#555;
  --line:#d9d9d9;
  --gray-bg:#f4f4f4;
  --footer:#111111;
  --white:#ffffff;
}
*{box-sizing:border-box;margin:0;padding:0}
html,body{width:1200px;height:5121px;overflow:hidden}
body{position:relative;font-family:"Noto Serif",Georgia,serif;color:var(--ink);background:var(--white)}
.abs{position:absolute}
.btn{position:absolute;display:flex;align-items:center;justify-content:center;border-radius:22px;font-size:12px;font-weight:700;letter-spacing:1px;text-transform:uppercase}
.btn-lime{background:var(--lime);color:var(--white)}
.btn-dark{background:#111;color:var(--white)}
.btn-outline{border:2px solid var(--lime);color:var(--lime);background:var(--white)}
.btn-green{background:var(--green);color:var(--white)}

.brand{left:109px;top:10px;display:flex;align-items:center;gap:8px}
.brand-dot{width:34px;height:34px;border-radius:50%;background:var(--lime)}
.brand-name{font-size:15px;font-weight:700;color:var(--green);line-height:1.1;width:60px}
.phone{left:490px;top:30px;display:flex;align-items:center;gap:12px;font-size:18px}
.phone-ico{width:30px;height:30px;border-radius:50%;background:var(--lime);display:flex;align-items:center;justify-content:center}
.nav{left:0;top:90px;width:1200px;height:46px;background:var(--green)}
.nav span{position:absolute;top:15px;color:var(--white);font-size:13px}

.hero-bg{left:0;top:136px;width:1200px;height:560px;background:linear-gradient(90deg,#d9ecd0 0%,#a8d48e 30%,#5fae45 60%,#2f7d2b 100%)}
.hero-title{left:109px;top:322px;font-size:28px;line-height:34px;font-weight:700;letter-spacing:1px;color:#111}
.hero-sub{left:109px;top:404px;font-size:14px;color:#111}
.green-band{left:0;top:700px;width:1200px;height:260px;background:var(--green)}

.card{top:825px;width:306px;height:362px;background:var(--white);border:1px solid var(--line);border-radius:8px;overflow:hidden}
.card-img{width:100%;height:238px}
.card h3{text-align:center;font-size:16px;font-weight:700;letter-spacing:1px;margin-top:24px;line-height:22px}
.card p{text-align:center;font-size:11px;line-height:18px;color:var(--muted);margin-top:6px}
.card-featured{background:var(--lime);border-color:var(--lime);box-shadow:0 8px 18px rgba(0,0,0,.2)}
.card-featured h3,.card-featured p{color:var(--white)}

.section-title{left:0;width:1200px;text-align:center;letter-spacing:2px}
.diamond{position:absolute;background:var(--green);border:3px solid var(--lime);border-radius:12px;transform:rotate(45deg)}
.diamond-label{position:absolute;text-align:center;color:var(--white);font-size:14px;font-weight:700;line-height:18px;display:flex;flex-direction:column;align-items:center;gap:8px}

.about{left:0;top:2050px;width:1200px;height:634px;background:var(--gray-bg)}
.h2{font-size:26px;font-weight:700;letter-spacing:2px}
.rule{height:3px;width:56px;background:var(--lime)}
.body-text{font-size:12.5px;line-height:20px;color:var(--muted)}

.field{position:absolute;border:1px solid var(--line);border-radius:3px;font-size:12px;color:#777;padding:14px 20px;background:var(--white)}
.check{display:flex;align-items:center;gap:6px;font-size:12px;color:#666;height:26px}
.check i{width:9px;height:9px;border:1px solid #888;display:inline-block}

.promo{left:0;top:3441px;width:1200px;height:628px;background:var(--green)}
.promo-box{left:161px;top:3918px;width:877px;height:300px;background:var(--lime);border-radius:10px}
.promo-box h2{position:absolute;left:0;top:72px;width:100%;text-align:center;color:var(--white);font-size:27px;line-height:40px;letter-spacing:1px}

.client{top:4431px;width:178px;height:107px;border:1px solid var(--line);display:flex;align-items:center;justify-content:center;font-size:15px;font-weight:700;color:var(--ink);text-align:center}

.footer{left:0;top:4668px;width:1200px;height:453px;background:var(--footer)}
.f-head{position:absolute;top:4758px;color:var(--white);font-size:15px;font-weight:700;letter-spacing:1.5px}
.f-text{position:absolute;color:#ddd;font-size:11.5px;line-height:17.5px}
.f-links span{display:block;line-height:21.5px}
.social{top:4958px;width:60px;height:32px;border-radius:3px;display:flex;align-items:center;justify-content:center;color:var(--white);font-size:10px;font-weight:700}
.copyright{left:109px;top:5084px;font-size:12px;color:#ddd}
.copyright b{color:var(--lime);font-weight:400}
</style>
</head>
<body>

<div class="abs brand"><span class="brand-dot"></span><span class="brand-name">7 Tall Harbor</span></div>
<div class="abs phone">
  <span class="phone-ico"><svg width="14" height="14" viewBox="0 0 24 24"><path d="M6.6 10.8a15 15 0 0 0 6.6 6.6l2.2-2.2a1 1 0 0 1 1-.25 11.4 11.4 0 0 0 3.6.57 1 1 0 0 1 1 1V20a1 1 0 0 1-1 1A17 17 0 0 1 3 4a1 1 0 0 1 1-1h3.5a1 1 0 0 1 1 1c0 1.25.2 2.45.57 3.57a1 1 0 0 1-.25 1z" fill="#fff"/></svg></span>
  (206) 555 - 0147
</div>
<div class="btn btn-lime" style="left:747px;top:24px;width:163px;height:42px">Pick Up</div>
<div class="btn btn-dark" style="left:926px;top:24px;width:165px;height:42px">Drop Off</div>

<nav class="abs nav">
  <span style="left:109px">IT Asset Disposition</span>
  <span style="left:292px">Electronics Recycling &#8964;</span>
  <span style="left:505px">Secure Data Destruction</span>
  <span style="left:723px">Product Destruction</span>
  <span style="left:912px">About &#8964;</span>
  <span style="left:1017px">Contact Us</span>
</nav>

<div class="abs hero-bg" role="img" aria-label="Photo of cupped hands holding soil, a sprouting plant and a small globe on a green background"></div>
<h1 class="abs hero-title">CERTIFIED E-RECYCLING<br>MADE EASY.</h1>
<p class="abs hero-sub">Reuse &amp; Recycle 99.9% of all materials we receive.</p>
<div class="btn btn-green" style="left:109px;top:452px;width:201px;height:40px;border:2px solid var(--lime);font-size:11px">Items We Recycle</div>

<div class="abs green-band"></div>
<svg class="abs" style="left:0;top:676px" width="1200" height="40" viewBox="0 0 1200 40">
  <path d="M0 28 H170 Q185 28 200 14 H1000 Q1015 28 1030 28 H1200 V40 H0Z" fill="#179a47"/>
  <path d="M0 28 H170 Q185 28 200 14 H1000 Q1015 28 1030 28 H1200" fill="none" stroke="#85c227" stroke-width="3"/>
</svg>

<div class="abs card" style="left:109px">
  <div class="card-img" role="img" aria-label="Photo of a green recycling bin filled with old electronics" style="background:linear-gradient(135deg,#5a3a2a,#2e9b3c 55%,#2a2a2a)"></div>
  <h3>BIN Program</h3>
  <p>Fill up our Bin at Your Location, when done,<br>we come and pick up!</p>
</div>
<div class="abs card card-featured" style="left:447px">
  <div class="card-img" role="img" aria-label="Photo of a crane loading scrap metal onto a truck at a recycling yard" style="background:linear-gradient(180deg,#9fb9cc,#7a6a5a 55%,#4a4a3e)"></div>
  <h3>Same Day Pickups<br>Available</h3>
  <p>Secure Chain of Custody</p>
</div>
<div class="abs card" style="left:785px">
  <div class="card-img" role="img" aria-label="Photo of an open hard drive breaking apart on a dark background" style="background:radial-gradient(circle at 45% 55%,#8f9aa6,#2a3440 55%,#0c1218)"></div>
  <h3>On-site<br>Data Destruction</h3>
</div>

<h2 class="abs section-title" style="top:1290px;font-size:26px;font-weight:400;line-height:34px">SAVE TIME. SAVE MONEY.<br><b>SAVE THE PLANET.</b></h2>

<div class="diamond" style="left:509px;top:1427px;width:174px;height:174px"></div>
<div class="diamond-label" style="left:496px;top:1474px;width:200px">
  <svg width="38" height="34" viewBox="0 0 38 34" fill="none" stroke="#fff" stroke-width="2"><path d="M8 18v-4a11 11 0 0 1 22 0v4"/><rect x="4" y="16" width="6" height="9" rx="2"/><rect x="28" y="16" width="6" height="9" rx="2"/><path d="M31 25q0 5-9 5"/><circle cx="15" cy="17" r="1.4" fill="#fff"/><circle cx="19" cy="17" r="1.4" fill="#fff"/><circle cx="23" cy="17" r="1.4" fill="#fff"/></svg>
  Quick Response
</div>
<svg class="abs" style="left:592px;top:1662px" width="16" height="46" viewBox="0 0 16 46"><path d="M8 0V42M1 35l7 8 7-8" fill="none" stroke="#179a47" stroke-width="2"/></svg>

<div class="diamond" style="left:141px;top:1747px;width:157px;height:157px"></div>
<div class="diamond-label" style="left:129px;top:1782px;width:180px">
  <svg width="34" height="34" viewBox="0 0 34 34" fill="none" stroke="#fff" stroke-width="2"><rect x="3" y="6" width="26" height="24" rx="2"/><path d="M3 12h26M10 3v6M22 3v6"/><circle cx="25" cy="25" r="6" fill="#179a47"/><path d="M25 22v3h3"/></svg>
  Immediate<br>Scheduling
</div>
<div class="diamond" style="left:399px;top:1747px;width:157px;height:157px"></div>
<div class="diamond-label" style="left:387px;top:1782px;width:180px">
  <svg width="34" height="34" viewBox="0 0 34 34" fill="none" stroke="#fff" stroke-width="2"><circle cx="16" cy="16" r="12"/><path d="M16 9v7l5 3"/><circle cx="26" cy="26" r="5" fill="#179a47"/><path d="M23.5 26l2 2 3-3.5"/></svg>
  On-time Secure<br>Pickup
</div>
<div class="diamond" style="left:643px;top:1747px;width:157px;height:157px"></div>
<div class="diamond-label" style="left:631px;top:1782px;width:180px">
  <svg width="34" height="34" viewBox="0 0 34 34" fill="none" stroke="#fff" stroke-width="2"><path d="M10 8a12 12 0 0 1 18 6M28 14l1-6M28 14l-6-1"/><path d="M24 27a12 12 0 0 1-18-5M6 22l-1 6M6 22l6 0"/></svg>
  Certified Recycling<br>Process
</div>
<div class="diamond" style="left:902px;top:1747px;width:157px;height:157px"></div>
<div class="diamond-label" style="left:890px;top:1772px;width:180px">
  <svg width="44" height="34" viewBox="0 0 44 34" fill="none" stroke="#fff" stroke-width="2"><circle cx="12" cy="10" r="7"/><path d="M9 10l2 2 4-4"/><path d="M18 18h14l6 6v5H18z"/><circle cx="23" cy="30" r="2.5"/><circle cx="34" cy="30" r="2.5"/></svg>
  Certifications &amp;<br>Asset Tracking<br>Delivered
</div>
<svg class="abs" style="left:310px;top:1750px" width="700" height="50" viewBox="0 0 700 50" fill="none" stroke="#85c227" stroke-width="2" stroke-dasharray="5 4">
  <path d="M0 28Q40 -5 78 36"/><path d="M262 28Q300 -5 338 36"/><path d="M508 28Q546 -5 584 36"/>
</svg>

<div class="abs about"></div>
<h2 class="abs h2" style="left:109px;top:2184px">WHO WE ARE</h2>
<div class="abs rule" style="left:109px;top:2228px"></div>
<p class="abs body-text" style="left:109px;top:2262px;width:460px">We are here for our community. We help the community by offering free drop-off</p>
<p class="abs body-text" style="left:109px;top:2324px;width:460px">To put it simply: if there is a cord attached, we can recycle it. From computers to photocopiers to washers and dryers, and far far more… we'll help you.</p>
<p class="abs" style="left:109px;top:2404px;font-size:13px;font-weight:700;color:#333">Pounds Recycled:</p>
<p class="abs body-text" style="left:109px;top:2432px">2020 - 7 million pounds<br>2019 - 6 million pounds</p>
<p class="abs body-text" style="left:310px;top:2432px">2018 - 5 million pounds<br>2017 - 4 million pounds</p>
<div class="btn btn-lime" style="left:109px;top:2510px;width:187px;height:34px;font-size:10px">About Us</div>
<div class="btn btn-outline" style="left:312px;top:2510px;width:187px;height:34px;font-size:10px">Items We Recycle</div>
<div class="abs" role="img" aria-label="Black and white photo of two workers sorting electronics in a recycling facility" style="left:642px;top:2163px;width:449px;height:411px;border-radius:10px;background:linear-gradient(135deg,#d8d8d8,#7a7a7a 50%,#2e2e2e)"></div>

<h2 class="abs section-title h2" style="top:2793px">CONTACT US</h2>
<div class="abs rule" style="left:572px;top:2836px"></div>
<div class="abs" role="img" aria-label="Street map showing the 7 Tall Harbor location" style="left:109px;top:2900px;width:463px;height:426px;border:1px solid var(--line);border-radius:6px;background:linear-gradient(160deg,#eef1ea,#d7e4ea 45%,#e8ece3)"></div>
<div class="field" style="left:618px;top:2900px;width:233px;height:44px">Name</div>
<div class="field" style="left:858px;top:2900px;width:233px;height:44px">Phone</div>
<div class="field" style="left:618px;top:2963px;width:473px;height:45px">Enter your email</div>
<div class="field" style="left:618px;top:3027px;width:473px;height:127px;padding:10px 20px">
  <div class="check"><i></i>Electronics Recycling</div>
  <div class="check"><i></i>Equipment &amp; Product Destruction</div>
  <div class="check"><i></i>Secure Data Destruction</div>
  <div class="check"><i></i>IT Asset Disposition</div>
</div>
<div class="field" style="left:618px;top:3174px;width:473px;height:88px">Message…</div>
<div class="btn btn-lime" style="left:618px;top:3284px;width:473px;height:42px;border-radius:2px;font-size:11px">Submit</div>

<div class="abs promo"></div>
<svg class="abs" style="left:280px;top:3441px" width="640" height="628" viewBox="0 0 640 628" fill="none" stroke="rgba(255,255,255,.2)" stroke-width="1.5">
  <circle cx="320" cy="240" r="200"/><circle cx="320" cy="240" r="240"/>
</svg>
<div class="abs" role="img" aria-label="Illustration of a white box truck carrying the company name" style="left:348px;top:3548px;width:507px;height:319px;border-radius:12px;background:linear-gradient(180deg,#ffffff,#e4e9e6 70%,#5a5a5a)"></div>
<div class="abs promo-box">
  <h2>Save time and disposal costs. We pick up loads<br>of E-Waste over 500 lbs for free!</h2>
</div>
<div class="btn btn-green" style="left:320px;top:4093px;width:268px;height:50px;border-radius:25px;font-size:13px">Items We Recycle</div>
<div class="btn btn-outline" style="left:612px;top:4093px;width:268px;height:50px;border-radius:25px;font-size:13px;color:var(--green);border-color:var(--white)">Schedule a Pickup</div>

<h2 class="abs section-title h2" style="top:4326px">OUR LOCAL CLIENTS</h2>
<div class="abs client" style="left:109px">Ridgeline Gear</div>
<div class="abs client" style="left:310px;box-shadow:0 4px 12px rgba(0,0,0,.15)">Harborview Inns</div>
<div class="abs client" style="left:511px">Sound Tides</div>
<div class="abs client" style="left:712px">Sunfan Co</div>
<div class="abs client" style="left:913px">Skyward Air</div>

<svg class="abs" style="left:0;top:4640px" width="1200" height="30" viewBox="0 0 1200 30">
  <path d="M0 22 H170 Q185 22 200 8 H1000 Q1015 22 1030 22 H1200 V30 H0Z" fill="#111"/>
  <path d="M0 22 H170 Q185 22 200 8 H1000 Q1015 22 1030 22 H1200" fill="none" stroke="#85c227" stroke-width="3"/>
</svg>
<div class="abs footer"></div>

<div class="f-head" style="left:109px">OUR PROMISE</div>
<p class="f-text" style="left:109px;top:4800px;width:200px">To provide E-Waste Recycling to EVERYONE!</p>
<div class="abs" style="left:109px;top:4872px;display:flex;gap:14px;align-items:center">
  <span style="width:60px;height:44px;border-radius:50%;background:#2c8a3c"></span>
  <span style="width:40px;height:40px;border-radius:50%;border:2px solid #ccc"></span>
  <span style="width:72px;height:34px;border-radius:17px;background:#2c8a3c"></span>
</div>
<div class="abs" style="left:109px;top:4952px;display:flex;gap:20px">
  <span style="width:112px;height:36px;background:#3d8f3d;border-radius:3px"></span>
  <span style="width:50px;height:40px;background:#e88a1a"></span>
</div>

<div class="f-head" style="left:386px">OUR MISSION</div>
<p class="f-text" style="left:386px;top:4800px;width:240px">We are a socially conscious recycling company that's fully committed to helping community, including small &amp; large business, with a one-stop solution for the responsible disposal of E-Waste.</p>
<p class="f-text" style="left:386px;top:4922px;width:240px">Local and Sustainable<br>0% waste<br>0% landfill<br>100% Environmental Conscious!</p>

<div class="f-head" style="left:697px">SITEMAP</div>
<div class="f-text f-links" style="left:697px;top:4796px">
  <span>Home</span><span>How It Works</span><span>Environment</span><span>Community</span><span>About</span><span>FAQs</span><span>Blog</span><span>Contact</span><span>Request a Pickup</span>
</div>

<div class="f-head" style="left:888px">CONNECT WITH US</div>
<svg class="abs" style="left:888px;top:4806px" width="20" height="20" viewBox="0 0 20 20"><circle cx="10" cy="10" r="10" fill="#85c227"/><path d="M10 4a4 4 0 0 0-4 4c0 3 4 8 4 8s4-5 4-8a4 4 0 0 0-4-4z" fill="#fff"/><circle cx="10" cy="8" r="1.5" fill="#85c227"/></svg>
<p class="f-text" style="left:918px;top:4806px">412 Alder Quay Road<br>Suite C<br>Kestrel Falls, KF 00417</p>
<svg class="abs" style="left:888px;top:4898px" width="20" height="20" viewBox="0 0 20 20"><circle cx="10" cy="10" r="10" fill="#85c227"/><path d="M7.5 9.5a7 7 0 0 0 3 3l1-1 2 .6V14a.6.6 0 0 1-.6.6A8 8 0 0 1 5.4 6.6.6.6 0 0 1 6 6h1.8l.6 2z" fill="#fff"/></svg>
<p class="f-text" style="left:918px;top:4898px">(206) 555-0147<br>(888) 555-0192</p>
<div class="abs social" style="left:888px;background:#2d62c8">Folkly</div>
<div class="abs social" style="left:960px;background:#e04433">Seekly</div>
<div class="abs social" style="left:1031px;background:#1da1f2">Chirpy</div>

<div class="abs" style="left:0;top:5060px;width:1200px;height:1px;background:#333"></div>
<p class="abs copyright">© Copyright 2021 • <b>7 Tall Harbor</b> • All Rights Reserved.</p>
<p class="abs copyright" style="left:984px">Privacy Policy</p>

</body>
</html>
```